Business card for plumber

I need a business card for my plumbing company.
on it should:
Surname
position
E-mail
Telephone & mobile phone
Website
Please everything as placeholders / fantasy names.
We stand for high quality, hygiene and professionalism.

Colours:
# 606060 anthracite
# f7931e orange
# 2b89cc blue

Industry/Entity Type

Plumber

Contact Information for Business Card

folgt...

```html
<!DOCTYPE html>
<html lang="en">
<head>
<meta charset="utf-8">
<title>Kellner Haustechnik – Business Card</title>
<link href="https://fonts.googleapis.com/css2?family=Roboto:wght@400;500;700;900&display=swap" rel="stylesheet">
<style>
  :root {
    --anthracite: #606060;
    --orange: #f7931e;
    --blue: #2b89cc;
    --blue-light: #5aaee0;
    --paper: #ffffff;
    --backdrop: #262626;
    --ink: #4a4a4a;
  }
  * { box-sizing: border-box; margin: 0; padding: 0; }
  html, body {
    width: 1200px; height: 929px; overflow: hidden;
    background: var(--backdrop);
    font-family: "Roboto", Arial, sans-serif;
  }
  .stage { position: relative; width: 1200px; height: 929px; }

  .card {
    position: absolute;
    width: 580px; height: 332px;
    border-radius: 16px;
    overflow: hidden;
    box-shadow: 0 18px 40px rgba(0,0,0,.55);
  }

  /* Front */
  .card--front {
    left: 70px; top: 80px;
    background: linear-gradient(160deg, var(--blue) 0%, #3f97d4 55%, var(--blue-light) 100%);
    display: flex; align-items: center; justify-content: center;
  }
  .brand { display: flex; align-items: center; gap: 14px; }
  .brand__dot {
    width: 46px; height: 46px; border-radius: 50%;
    flex: none;
  }
  .brand__name {
    font-weight: 900; text-transform: uppercase;
    font-size: 28px; line-height: 1.05; letter-spacing: .5px;
  }
  .brand__name span { display: block; }
  .card--front .brand__dot { background: var(--orange); }
  .card--front .brand__name { color: var(--paper); }

  /* Back */
  .card--back {
    left: 550px; top: 520px;
    background: var(--paper);
  }
  .card--back .brand {
    position: absolute; left: 40px; top: 138px;
  }
  .card--back .brand__dot { background: var(--orange); width: 40px; height: 40px; }
  .card--back .brand__name { color: var(--blue); font-size: 22px; }

  .divider {
    position: absolute; left: 318px; top: 70px;
    width: 1.5px; height: 168px; background: var(--anthracite);
  }
  .contact { position: absolute; left: 340px; top: 68px; }
  .contact__name {
    color: var(--blue); font-weight: 700; font-size: 20px;
    text-transform: uppercase; letter-spacing: -.2px;
  }
  .contact__role {
    color: var(--orange); font-weight: 500; font-size: 17px; margin-top: 1px;
  }
  .contact__list { list-style: none; margin-top: 12px; }
  .contact__list li {
    display: flex; align-items: center; gap: 8px;
    color: var(--ink); font-size: 15px; line-height: 23px;
  }
  .contact__list svg { width: 15px; height: 15px; flex: none; }

  .band {
    position: absolute; left: 0; bottom: 0;
    width: 100%; height: 12px;
  }
</style>
</head>
<body>
<main class="stage">

  <section class="card card--front" aria-label="Card front">
    <div class="brand">
      <span class="brand__dot"></span>
      <div class="brand__name"><span>Kellner</span><span>Haustechnik</span></div>
    </div>
  </section>

  <section class="card card--back" aria-label="Card back">
    <div class="brand">
      <span class="brand__dot"></span>
      <div class="brand__name"><span>Kellner</span><span>Haustechnik</span></div>
    </div>

    <div class="divider"></div>

    <div class="contact">
      <h1 class="contact__name">Lukas Brennwald</h1>
      <p class="contact__role">Managing Director</p>
      <ul class="contact__list">
        <li>
          <svg viewBox="0 0 16 16" aria-hidden="true"><rect x="4" y="1" width="8" height="14" rx="1.5" fill="none" stroke="var(--blue)" stroke-width="1.5"/><circle cx="8" cy="12.5" r=".9" fill="var(--blue)"/></svg>
          555.214.7830
        </li>
        <li>
          <svg viewBox="0 0 16 16" aria-hidden="true"><path d="M1 6c0-3 14-3 14 0v1.5h-3.5V6h-7v1.5H1z" fill="var(--blue)"/><path d="M3 9h10l1 5H2z" fill="var(--blue)"/></svg>
          555.608.4419
        </li>
        <li>
          <svg viewBox="0 0 16 16" aria-hidden="true"><rect x="1" y="3" width="14" height="10" fill="var(--blue)"/><path d="M1 3l7 6 7-6" fill="none" stroke="#fff" stroke-width="1.3"/></svg>
          info@kellnerhk.com
        </li>
        <li>
          <svg viewBox="0 0 16 16" aria-hidden="true"><circle cx="8" cy="8" r="7" fill="var(--blue)"/><path d="M8 1v14M1 8h14M8 1c-4 3-4 11 0 14M8 1c4 3 4 11 0 14" fill="none" stroke="#fff" stroke-width=".9"/></svg>
          www.kellnerhk.com
        </li>
      </ul>
    </div>

    <svg class="band" viewBox="0 0 580 12" preserveAspectRatio="none" aria-hidden="true">
      <polygon points="0,0 322,0 316,12 0,12" fill="var(--blue)"/>
      <polygon points="326,0 580,0 580,12 320,12" fill="var(--orange)"/>
    </svg>
  </section>

</main>
</body>
</html>
```